Business Cards Needed For Veterinary Business

Looking for a business card design for a veterinary blood bank. We would like it to be clean and professional on appearance but still warm and inviting. We would like to utilize our logo and similar coloring. We will use our phone number, email, website, employee name, employee title.

We do not want a bunch of animated animal photos but do not need the style to be as clinical as a laboratory or human medical procedure office.

We are looking for some creative ideas to choose from so that we can generate a standout professional business card for our management team to utilize.

Target Market(s)

professionals

Industry/Entity Type

veterinary

Contact Information for Business Card

employee name, employee title, phone number, website URL, email

Font styles to use
Sans Serif

Colors
0054AA
0677BA
7BADD7
CADEEF
E8F1F8
EB3D1F
EC4F4E
F09395
F8D3D4
FCEDEE

Requirements
Nice to have
• creative design
Should not have
• animated photos

```html
<!DOCTYPE html>
<html lang="en">
<head>
<meta charset="utf-8">
<title>Great Plains Veterinary Blood Bank – Business Cards</title>
<link href="https://fonts.googleapis.com/css2?family=Montserrat:wght@400;500;700;800&display=swap" rel="stylesheet">
<style>
  :root {
    --bg: #3a3a3a;
    --card-white: #ffffff;
    --card-black: #141414;
    --brand-red: #e31b23;
    --brand-blue: #0d4f99;
    --brand-grey: #6d6d6d;
    --contact-text: #f2f2f2;
    --title-text: #222222;
  }
  * { margin: 0; padding: 0; box-sizing: border-box; }
  html, body { width: 1200px; height: 780px; overflow: hidden; }
  body {
    background: var(--bg);
    font-family: "Montserrat", sans-serif;
    display: flex;
    align-items: center;
    justify-content: center;
    gap: 60px;
  }
  .card {
    position: relative;
    width: 540px;
    height: 310px;
    border-radius: 22px;
    overflow: hidden;
    background: var(--card-white);
    box-shadow: 0 14px 34px rgba(0,0,0,.45);
  }
  .card-waves { position: absolute; inset: 0; width: 100%; height: 100%; }

  .holder {
    position: absolute;
    top: 22px;
    left: 0;
    display: flex;
    align-items: flex-start;
    z-index: 1;
  }
  .holder-marker {
    width: 30px;
    height: 26px;
    background: var(--brand-red);
    margin-right: 12px;
  }
  .holder-name {
    color: var(--brand-red);
    font-weight: 700;
    font-size: 20px;
    letter-spacing: .5px;
    line-height: 1.1;
  }
  .holder-title {
    color: var(--title-text);
    font-size: 12px;
    font-weight: 400;
    margin-top: 3px;
  }

  .contact {
    position: absolute;
    left: 24px;
    bottom: 24px;
    color: var(--contact-text);
    font-size: 12px;
    line-height: 1.55;
    list-style: none;
    z-index: 1;
  }
  .contact-address { margin-left: 22px; margin-bottom: 6px; }
  .contact-item { display: flex; align-items: center; gap: 8px; }
  .contact-icon { width: 14px; height: 14px; flex: none; }

  .brand {
    position: absolute;
    display: flex;
    align-items: center;
    gap: 12px;
  }
  .brand-dot {
    flex: none;
    border-radius: 50%;
    background: var(--brand-red);
  }
  .brand-name {
    color: var(--brand-red);
    font-weight: 800;
    text-transform: uppercase;
    line-height: 1.05;
  }
  .card-front .brand { right: 26px; top: 150px; }
  .card-front .brand-dot { width: 22px; height: 22px; }
  .card-front .brand-name { font-size: 19px; width: 200px; }

  .card-back .brand { left: 50%; top: 50%; transform: translate(-50%, -50%); }
  .card-back .brand-dot { width: 34px; height: 34px; }
  .card-back .brand-name { font-size: 30px; width: 330px; }
</style>
</head>
<body>

  <section class="card card-front">
    <svg class="card-waves" viewBox="0 0 540 310" preserveAspectRatio="none" aria-hidden="true">
      <path d="M0 115 C100 118 165 150 195 215 C220 270 290 300 400 310 L0 310 Z" fill="var(--card-black)"/>
      <path d="M0 105 C110 108 180 145 212 212 C240 268 320 300 440 310 L400 310 C290 300 220 270 195 215 C165 150 100 118 0 115 Z" fill="var(--brand-red)"/>
      <path d="M0 86 C120 88 200 128 238 200" fill="none" stroke="var(--brand-blue)" stroke-width="5"/>
      <path d="M60 97 C150 101 205 135 230 190" fill="none" stroke="var(--brand-red)" stroke-width="2"/>
    </svg>

    <div class="holder">
      <span class="holder-marker"></span>
      <div>
        <p class="holder-name">DANIEL REYES</p>
        <p class="holder-title">Managing Director</p>
      </div>
    </div>

    <ul class="contact">
      <li class="contact-address">Your address, City<br>State, Zip 1234</li>
      <li class="contact-item">
        <svg class="contact-icon" viewBox="0 0 16 16" aria-hidden="true"><circle cx="8" cy="8" r="8" fill="var(--brand-red)"/><path d="M5 4.5l1.6-.4.9 2-1 .8a5 5 0 0 0 2.6 2.6l.8-1 2 .9-.4 1.6c-3.6.2-6.7-2.9-6.5-6.5z" fill="#fff"/></svg>
        123 456 789
      </li>
      <li class="contact-item">
        <svg class="contact-icon" viewBox="0 0 16 16" aria-hidden="true"><circle cx="8" cy="8" r="8" fill="var(--brand-red)"/><rect x="4" y="5" width="8" height="6" fill="#fff"/><path d="M4 5l4 3.2L12 5" fill="none" stroke="var(--brand-red)" stroke-width="1"/></svg>
        info@yourgmail.com
      </li>
      <li class="contact-item">
        <svg class="contact-icon" viewBox="0 0 16 16" aria-hidden="true"><circle cx="8" cy="8" r="8" fill="var(--brand-red)"/><circle cx="8" cy="8" r="4.2" fill="none" stroke="#fff" stroke-width="1.1"/><path d="M3.8 8h8.4M8 3.8c-2 2.5-2 5.9 0 8.4M8 3.8c2 2.5 2 5.9 0 8.4" fill="none" stroke="#fff" stroke-width=".9"/></svg>
        www.yourwebsite.com
      </li>
    </ul>

    <div class="brand">
      <span class="brand-dot"></span>
      <p class="brand-name">Great Plains Veterinary Blood Bank</p>
    </div>
  </section>

  <section class="card card-back">
    <div class="brand">
      <span class="brand-dot"></span>
      <p class="brand-name">Great Plains Veterinary Blood Bank</p>
    </div>
  </section>

</body>
</html>
```